Brochure Design Project

We need a brochure designed to introduce a new professional fitness testing programme we are launching. We are an established health and fitness club based in Wiltshire, England. We would like each design to use the company colours which are white, black and blue. We offer a premier service which we want the brochure to illustrate. We would like the brochure to be 4 x A5 pages (A4 paper folded in half) and landscape. We have attached a word document with the wording we want included and our company logo. Although we have placed page numbers at the bottom of each A5 side in the brief please do not include these in the brochure, this is simply to illustrate the order of the pages. What we need is for you to give the brochure colour, artwork and a professional touch while emphasising key points.
Updates

APOLIGIES TO ALL DESIGNERS....... please could the brochure be portrait.

Many thanks

Amber Wren UK

Can we please have the desgines aimed more at amateur athletes as this is the market we are aiming at

thank you

More designs welcomed!

Reason: Very little designs recieved

Designers, thankyou soo much for your designs soo far. What we would like too see is rather than pictures of women and commercial images can we have images of professional looking cyclists please. many thanks

Target Market(s)

amateur fitness enthusiasts (male and female) between the ages of 25-50, in the upper socio-economic sector of society.

Industry/Entity Type

Fitness

Requirements
Must have
• The brochure must include the company logo and be 4 A5 lanscape pages (A4 folded in half). Only use the company colours: white, black and blue. (the blue is the colour on the website which is on the attatched word document/design brief). Must include pictures of professional looking cyclists and runners.
Nice to have
• A front page which is really creative and bold, which sells our service to the buyer in a respectable way.
Should not have
• Cheesey pictures.

```html
<!DOCTYPE html>
<html lang="en">
<head>
<meta charset="utf-8">
<title>Amber Wren UK – Fitness Assessment</title>
<link rel="stylesheet" href="https://fonts.googleapis.com/css2?family=Oswald:wght@400;500&family=Roboto+Slab:wght@700&family=Roboto+Condensed:wght@300;400&display=swap">
<style>
  :root {
    --strip: #aeb6d6;
    --ink-white: #ffffff;
    --bar: #0b0b0b;
    --bar-text: #c9c9c9;
    --stage-blue-1: rgba(86, 140, 190, 0.85);
    --stage-blue-2: rgba(44, 102, 168, 0.86);
    --stage-blue-3: rgba(22, 66, 130, 0.88);
    --stage-blue-4: rgba(10, 34, 78, 0.88);
    --number-ring: #ffffff;
    --number-fill: #000000;
    --sky-top: #0f2236;
    --sky-mid: #4c6d8e;
    --sky-light: #a9bccd;
  }
  * { margin: 0; padding: 0; box-sizing: border-box; }
  html, body { width: 1200px; height: 851px; overflow: hidden; background: #fff; }
  .page {
    position: relative; width: 1200px; height: 851px; overflow: hidden;
    font-family: "Roboto Condensed", "Arial Narrow", sans-serif; color: var(--ink-white);
  }
  .backdrop {
    position: absolute; left: 0; top: 0; width: 1200px; height: 816px;
    background:
      linear-gradient(180deg, transparent 0%, transparent 78%, rgba(110,112,110,0.85) 88%, #4d4f52 100%),
      radial-gradient(ellipse at 50% 62%, var(--sky-light) 0%, var(--sky-mid) 38%, var(--sky-top) 80%);
  }
  .top-strip { position: absolute; left: 0; top: 0; width: 1200px; height: 22px; background: var(--strip); }
  .headline {
    position: absolute; left: 36px; top: 34px; font-size: 19px; font-weight: 300;
  }
  .headline-rule { position: absolute; left: 36px; top: 64px; width: 1130px; height: 1px; background: var(--ink-white); }
  .intro {
    position: absolute; left: 36px; top: 77px; width: 1135px;
    font-size: 13px; font-weight: 300; line-height: 21.6px;
  }
  .process-title {
    position: absolute; left: 36px; top: 170px;
    font-family: "Roboto Slab", Georgia, serif; font-weight: 700; font-size: 19px;
  }
  .stage {
    position: absolute; top: 214px; width: 267px; height: 576px;
    font-family: "Oswald", "Arial Narrow", sans-serif; text-align: center;
  }
  .stage-1 { left: 26px; background: var(--stage-blue-1); }
  .stage-2 { left: 307px; background: var(--stage-blue-2); }
  .stage-3 { left: 626px; background: var(--stage-blue-3); }
  .stage-4 { left: 907px; background: var(--stage-blue-4); }
  .stage-number {
    position: absolute; left: 100px; top: 19px; width: 66px; height: 66px;
    border-radius: 50%; background: var(--number-fill); border: 3px solid var(--number-ring);
    font-family: Arial, sans-serif; font-weight: 700; font-size: 40px; line-height: 60px; color: #fff;
  }
  .stage-title { position: absolute; left: 0; width: 100%; top: 133px; font-size: 26px; font-weight: 400; line-height: 1; }
  .stage-item { position: absolute; left: 0; width: 100%; font-size: 17px; font-weight: 500; line-height: 34px; }
  .footer {
    position: absolute; left: 0; top: 816px; width: 1200px; height: 35px; background: var(--bar);
    font-family: Arial, sans-serif; font-size: 10px; letter-spacing: 3px; color: var(--bar-text);
  }
  .footer-web { position: absolute; top: 12px; }
  .footer-web.left { left: 212px; }
  .footer-web.right { left: 812px; }
</style>
</head>
<body>
<div class="page">
  <div class="backdrop" role="img" aria-label="Photograph of a long open road stretching to the horizon under a dramatic blue cloudy sky"></div>
  <div class="top-strip"></div>

  <h1 class="headline">How do you get to where you want to be without knowing where you are...........</h1>
  <div class="headline-rule"></div>
  <p class="intro">At Amber Wren UK we care about your fitness goals, which is why we have introduced our new and exciting comprehensive fitness assessment. Our qualified exercise specialists are on hand to take you through our four stage process. Furthermore, the variety of testing protocols we utilise are all used by professional athletes. With our help, you can achieve your desired success and continuously develop. This is achieved through a combination of energy and direction as well as a balance between hard work and recovery.</p>

  <h2 class="process-title">Our four stage process.....</h2>

  <section class="stage stage-1">
    <div class="stage-number">1</div>
    <h3 class="stage-title">Pre Test analysis</h3>
    <div class="stage-item" style="top:199px">Includes.....</div>
    <div class="stage-item" style="top:247px">Body fat percentage</div>
    <div class="stage-item" style="top:295px">Lean mass calculation</div>
    <div class="stage-item" style="top:343px">Blood Pressure (ml/kg)</div>
    <div class="stage-item" style="top:391px">Pulse (bpm)</div>
    <div class="stage-item" style="top:436px">Cholesterol (measure)</div>
    <div class="stage-item" style="top:484px">Lung function assessment (FEV1)</div>
  </section>

  <section class="stage stage-2">
    <div class="stage-number">2</div>
    <h3 class="stage-title">Fitness test</h3>
    <div class="stage-item" style="top:199px">(Cycling, Running or rowing)</div>
    <div class="stage-item" style="top:260px">Vo2 max (ml/kg/g)</div>
    <div class="stage-item" style="top:323px">Lactate threshold</div>
    <div class="stage-item" style="top:385px">Cardiovascular efficiency</div>
    <div class="stage-item" style="top:447px">Pedalling assessment for cyclists</div>
    <div class="stage-item" style="top:508px">Flexibility tests</div>
  </section>

  <section class="stage stage-3">
    <div class="stage-number">3</div>
    <h3 class="stage-title">Post test report</h3>
    <div class="stage-item" style="top:199px">Consultation with your<br>assigned specialist</div>
    <div class="stage-item" style="top:306px">Detailed test results</div>
    <div class="stage-item" style="top:375px">Comparisons made with<br>normative data</div>
    <div class="stage-item" style="top:473px">Concluding with areas<br>to develop</div>
  </section>

  <section class="stage stage-4">
    <div class="stage-number">4</div>
    <h3 class="stage-title">12 week programme</h3>
  </section>

  <footer class="footer">
    <span class="footer-web left">www.amberwrenfitness.com</span>
    <span class="footer-web right">www.amberwrenfitness.com</span>
  </footer>
</div>
</body>
</html>
```